Business Card Design for Varnok Facility Services

We are looking for a Business Card Design for the Company "Varnok Facility Services."
Front side:
- Company Logo (small)
- Company Name, address, pohone, website and personal data.
- white background, for text e.g. company colors (blue or green like in the logo)
Please use following data:
Company data:
Varnok Facility Services Tulbrecht
Kirchmattweg 12
6331 Cham
www.varnok-fs.ch
Person data:
Ruben Tulbrecht
Geschäftsführer
+41 76 519 84 60
info@varnok-fs.ch
Back side:
could be colored in blue or green
please use a big logo sing and some smaller icons to say what is all beeing offered in facility services, like cleaning, maintenance cleaning
industrial cleaning, caretaking, gardening, disposal. There is no need for everyone of the icons if there are similar or an icon is standing for more of them.
Cleaning Service
colors to use:
blue: HEX 246BB0
green: HEX 52B33E

```html
<!DOCTYPE html>
<html lang="de">
<head>
<meta charset="utf-8">
<title>Varnok Facility Services – Visitenkarte</title>
<link rel="stylesheet" href="https://fonts.googleapis.com/css2?family=Source+Sans+3:wght@400;600&display=swap">
<style>
  :root {
    --brand-blue: #246BB0;
    --brand-green: #52B33E;
    --panel-green: #5AB946;
    --card-white: #ffffff;
    --page-bg: #ffffff;
    --ink-light: #ffffff;
  }
  * { margin: 0; padding: 0; box-sizing: border-box; }
  html, body {
    width: 1200px; height: 960px; overflow: hidden;
    background: var(--page-bg);
    font-family: "Source Sans 3", "Source Sans Pro", sans-serif;
  }
  .canvas { position: relative; width: 1200px; height: 960px; }
  .card {
    position: absolute; left: 286px; width: 629px; height: 359px;
    background: var(--card-white);
    box-shadow: 0 2px 6px rgba(0,0,0,0.35);
    overflow: hidden;
  }
  .card--front { top: 109px; }
  .card--back { top: 492px; }
  .panel { position: absolute; left: 0; top: 0; width: 629px; height: 359px; }
  .wordmark {
    position: absolute; display: flex; align-items: center;
    color: var(--brand-blue); font-weight: 600; white-space: nowrap;
  }
  .wordmark__dot { border-radius: 50%; background: var(--brand-green); flex: none; }
  .wordmark--small { left: 30px; top: 166px; font-size: 19px; gap: 8px; }
  .wordmark--small .wordmark__dot { width: 16px; height: 16px; }
  .wordmark--large {
    left: 40px; top: 112px; width: 234px; flex-direction: column;
    font-size: 30px; line-height: 1.1; gap: 14px; text-align: center;
  }
  .wordmark--large .wordmark__dot { width: 46px; height: 46px; }
  .person { position: absolute; left: 351px; top: 87px; color: var(--ink-light); }
  .person__name { font-size: 23px; font-weight: 600; line-height: 1.2; }
  .person__role { font-size: 19px; font-weight: 400; line-height: 1.2; margin-top: 1px; }
  .person__rule { width: 49px; height: 2px; background: var(--ink-light); margin-top: 3px; }
  .contact-list { position: absolute; left: 351px; top: 168px; list-style: none; color: var(--ink-light); }
  .contact-list li {
    display: flex; align-items: center; height: 26px; font-size: 17px;
  }
  .contact-list svg { width: 17px; height: 17px; margin-right: 14px; flex: none; }
  .service-list { position: absolute; left: 365px; top: 101px; list-style: none; color: var(--ink-light); }
  .service-list li {
    display: flex; align-items: center; height: 26.3px; font-size: 17.5px;
  }
  .service-list svg { width: 15px; height: 15px; margin-right: 8px; flex: none; }
</style>
</head>
<body>
<div class="canvas">

  <section class="card card--front">
    <svg class="panel" viewBox="0 0 629 359" aria-hidden="true">
      <path d="M292 52 Q291 46 298 46 L629 46 L629 316 L360 316 Q336 316 332 292 Z" fill="var(--panel-green)"/>
    </svg>
    <div class="wordmark wordmark--small"><span class="wordmark__dot"></span>Varnok Facility Services</div>
    <div class="person">
      <div class="person__name">Ruben Tulbrecht</div>
      <div class="person__role">Geschäftsführer</div>
      <div class="person__rule"></div>
    </div>
    <ul class="contact-list">
      <li><svg viewBox="0 0 24 24"><path d="M6 2 L9 7 L7 9 Q9 14 15 17 L17 15 L22 18 L20 22 Q10 22 3 12 Q2 6 6 2 Z" fill="#fff"/></svg>+41 76 519 84 60</li>
      <li><svg viewBox="0 0 24 24"><rect x="2" y="5" width="20" height="14" fill="#fff"/><path d="M2 5 L12 13 L22 5 M2 19 L10 12 M22 19 L14 12" stroke="var(--panel-green)" stroke-width="1.6" fill="none"/></svg>info@varnok-fs.ch</li>
      <li><svg viewBox="0 0 24 24"><circle cx="12" cy="12" r="10" fill="#fff"/><path d="M4 9 Q10 11 12 6 M8 20 Q9 14 15 13 Q19 13 21 10" stroke="var(--panel-green)" stroke-width="2" fill="none"/></svg>www.varnok-fs.ch</li>
      <li><svg viewBox="0 0 24 24"><path d="M12 16 Q6 10 6 7 A6 6 0 0 1 18 7 Q18 10 12 16 Z" fill="none" stroke="#fff" stroke-width="2"/><circle cx="12" cy="7" r="2" fill="#fff"/><ellipse cx="12" cy="20" rx="9" ry="2.5" fill="none" stroke="#fff" stroke-width="2"/></svg>Kirchmattweg 12, 6331 Cham</li>
    </ul>
  </section>

  <section class="card card--back">
    <svg class="panel" viewBox="0 0 629 359" aria-hidden="true">
      <path d="M292 52 Q291 46 298 46 L629 46 L629 316 L360 316 Q336 316 332 292 Z" fill="var(--panel-green)"/>
    </svg>
    <div class="wordmark wordmark--large"><span class="wordmark__dot"></span><span>Varnok<br>Facility Services</span></div>
    <ul class="service-list">
      <li><svg viewBox="0 0 20 20"><path d="M10 0 Q11 9 20 10 Q11 11 10 20 Q9 11 0 10 Q9 9 10 0 Z" fill="#fff"/></svg>Like cleaning</li>
      <li><svg viewBox="0 0 20 20"><path d="M10 0 Q11 9 20 10 Q11 11 10 20 Q9 11 0 10 Q9 9 10 0 Z" fill="#fff"/></svg>Maintenance cleaning</li>
      <li><svg viewBox="0 0 20 20"><path d="M10 0 Q11 9 20 10 Q11 11 10 20 Q9 11 0 10 Q9 9 10 0 Z" fill="#fff"/></svg>Industrial cleaning</li>
      <li><svg viewBox="0 0 20 20"><path d="M10 0 Q11 9 20 10 Q11 11 10 20 Q9 11 0 10 Q9 9 10 0 Z" fill="#fff"/></svg>Caretaking</li>
      <li><svg viewBox="0 0 20 20"><path d="M10 0 Q11 9 20 10 Q11 11 10 20 Q9 11 0 10 Q9 9 10 0 Z" fill="#fff"/></svg>Gardening</li>
      <li><svg viewBox="0 0 20 20"><path d="M10 0 Q11 9 20 10 Q11 11 10 20 Q9 11 0 10 Q9 9 10 0 Z" fill="#fff"/></svg>Disposal</li>
    </ul>
  </section>

</div>
</body>
</html>
```